Massage-Creme label for a young pharmacy

We are a young pharmacy which is part of a big union. We developed for a customer a very good massage creme with aloe vera, coconut oil, and many more advantages and as well a massage jelly. All we need is a good and affordable label which is beatiful and helps us to promote our product. As we want to develop further products, it would be very cool to have a corporate label for all upcoming products.

Target Market(s)

professional masseurs and physiotherapists

Industry/Entity Type

Health And Wellness

Font styles to use
Sans Serif
Decorative

Colors

Designer to choose colors to be used in the design.

Requirements
Must have
• Professionally looking design (but I'm sure you are doing so... :-)
Nice to have
• Label can have any shape. What you see is just a bad label with corresponding sizes, so you can imagine how it would look like in the final state.
Should not have
• If possible, the label should not be completely black (although it might look cool) as we are printing it on our own Vostek qr318-ux and black is difficult to print (and very costy).

```html
<!DOCTYPE html>
<html lang="de">
<head>
<meta charset="utf-8">
<title>Massage Creme – Etikett</title>
<link rel="stylesheet" href="https://fonts.googleapis.com/css2?family=Varela+Round&family=Open+Sans:wght@400;600&family=Nothing+You+Could+Do&display=swap">
<style>
  :root {
    --page: #ffffff;
    --cream-light: #fdf8ee;
    --cream: #f5e8cf;
    --green-wash: #eef2d6;
    --leaf: #3f7a12;
    --brown: #8a4a1c;
    --brown-warm: #a35a1f;
    --ink: #4a4a4a;
    --band: rgba(255, 250, 240, 0.75);
    --art-green: #cfe2a8;
    --art-tan: #d9b68e;
  }
  * { margin: 0; padding: 0; box-sizing: border-box; }
  html, body {
    width: 1130px; height: 1200px; overflow: hidden;
    background: var(--page);
  }
  .label {
    position: absolute; left: 215px; top: 40px;
    width: 700px; height: 1120px; overflow: hidden;
    background:
      linear-gradient(90deg, var(--green-wash) 0%, rgba(238,242,214,0) 30%, rgba(238,242,214,0) 70%, var(--green-wash) 100%),
      linear-gradient(180deg, var(--cream-light) 0%, var(--cream) 55%, var(--cream-light) 100%);
    box-shadow: 6px 8px 10px rgba(0,0,0,0.18);
    font-family: "Open Sans", sans-serif;
  }
  .brand {
    position: absolute; left: 0; top: 40px; width: 430px; height: 132px;
    background: rgba(250, 240, 222, 0.85);
    padding: 26px 0 0 52px;
  }
  .brand__name {
    font-family: "Varela Round", sans-serif;
    font-size: 40px; letter-spacing: 3px; color: var(--ink); line-height: 1;
  }
  .brand__pharmacy {
    margin-top: 10px; margin-left: 90px;
    font-family: "Varela Round", sans-serif;
    font-size: 20px; letter-spacing: 1px; color: var(--ink);
  }
  .brand__tagline {
    margin-top: 6px; margin-left: 168px;
    font-size: 12px; letter-spacing: 1.5px; color: var(--ink);
  }
  .claim {
    position: absolute; left: 378px; top: 212px; width: 180px; height: 80px;
    background: var(--band); border-radius: 10px;
    padding: 10px 0 0 18px;
    font-family: "Varela Round", sans-serif; font-size: 26px; line-height: 1.2;
    color: var(--brown-warm);
  }
  .title {
    position: absolute; right: 135px; top: 306px;
    font-family: "Varela Round", sans-serif; font-size: 104px; line-height: 1.2;
    font-weight: 400;
    color: var(--leaf); text-align: right;
    text-shadow: 0 0 6px #fff, 0 0 10px #fff, 0 0 14px #fff;
  }
  .variant {
    position: absolute; left: 110px; top: 582px; width: 477px; height: 90px;
    border-top: 2px solid var(--leaf); border-bottom: 2px solid var(--leaf);
    display: flex; align-items: center; justify-content: center;
  }
  .variant__band {
    position: absolute; left: -30px; right: -30px; top: 10px; bottom: 10px;
    background: var(--band);
  }
  .variant__text {
    position: relative;
    font-family: "Nothing You Could Do", cursive; font-size: 48px;
    color: var(--brown); white-space: nowrap; letter-spacing: 1px;
  }
  .volume {
    position: absolute; left: 466px; top: 680px;
    font-size: 21px; color: var(--ink);
  }
  .illustration {
    position: absolute; left: 120px; top: 720px; width: 440px; height: 360px;
    border-radius: 24px;
    background: linear-gradient(180deg, var(--art-green) 0%, var(--art-tan) 100%);
    opacity: 0.7;
  }
</style>
</head>
<body>
  <main class="label">
    <header class="brand">
      <div class="brand__name">Medivia</div>
      <div class="brand__pharmacy">Apotheke Dr. Lindqvist</div>
      <div class="brand__tagline">DROGERIE &amp; PARFUMERIE</div>
    </header>

    <div class="claim">energetisch<br>leitend!</div>

    <h1 class="title">Massage<br>Creme</h1>

    <div class="variant">
      <div class="variant__band"></div>
      <span class="variant__text">Aloe Vera&nbsp; Coconut</span>
    </div>

    <div class="volume">℮ 1000 ml</div>

    <div class="illustration" role="img" aria-label="Illustration: Aloe-Vera-Pflanze, halbierte Kokosnüsse, Holzlöffel mit Creme und ein Öltropfen"></div>
  </main>
</body>
</html>
```